Banner/yard sign

Media blasting removal of many things from multiple surfaces-see attached note

Industry/Entity Type

Media

Logo Text

provided logo is done

Requirements
Must have
• Make sure all greens match green in original logo
• Use Tornado from Yard sign 6 file 5
• Use complete Logo with correct logo File 9

```html
<!DOCTYPE html>
<html lang="en">
<head>
<meta charset="utf-8">
<title>Halden Strip Co. – Yard Sign</title>
<link rel="stylesheet" href="https://fonts.googleapis.com/css2?family=Montserrat:wght@700&family=Oswald:wght@500;600;700&family=Russo+One&family=Audiowide&display=swap">
<style>
  :root {
    --green: #1a8a45;
    --green-dark: #137a3b;
    --green-bright: #22a650;
    --ink: #1a1a1a;
    --heading: #3a3a3a;
    --grey-light: #c4c8c6;
    --grey-dark: #7b7d7e;
    --white: #ffffff;
  }
  * { margin: 0; padding: 0; box-sizing: border-box; }
  html, body { width: 1200px; height: 900px; overflow: hidden; background: #fff; }
  .sign {
    position: relative; width: 1200px; height: 900px; overflow: hidden;
    background: linear-gradient(100deg, var(--grey-light) 0%, #b3b6b5 45%, var(--grey-dark) 100%);
    font-family: "Oswald", sans-serif;
  }
  .sector-bar {
    position: absolute; left: 0; top: 0; width: 1200px; height: 112px;
    background: linear-gradient(90deg, var(--green-dark), var(--green));
    display: flex; align-items: center; justify-content: space-between; padding: 0 80px 0 94px;
  }
  .sector { display: flex; align-items: center; gap: 26px; color: var(--white);
    font-family: "Montserrat", sans-serif; font-weight: 700; font-size: 31px; letter-spacing: 1px; }
  .sector svg { width: 66px; height: 66px; }
  .stripes { position: absolute; left: 0; top: 596px; width: 1200px; }
  .stripes span { display: block; height: 11px; margin-bottom: 9px; background: var(--green-dark); }
  .mascot {
    position: absolute; left: 20px; top: 184px; width: 476px; height: 624px;
    background: radial-gradient(ellipse at 45% 40%, #2aa556 0%, #178a42 55%, #0f4f27 100%);
    border-radius: 48% 52% 40% 60% / 40% 40% 60% 60%;
  }
  .col-head { position: absolute; top: 132px; font-family: "Russo One", sans-serif; font-weight: 400;
    font-style: italic; font-size: 30px; letter-spacing: 7px; color: var(--heading); line-height: 1; }
  .list { position: absolute; top: 190px; list-style: none; }
  .list li { display: flex; align-items: center; height: 31.3px; font-weight: 600; font-size: 27px;
    color: var(--ink); line-height: 1; }
  .list li svg { width: 36px; height: 30px; margin-right: 12px; flex: none; }
  .more { position: absolute; left: 560px; top: 462px; width: 554px; text-align: right;
    font-family: "Russo One", sans-serif; font-style: italic; font-size: 30px; line-height: 1;
    color: #2a2a2a; -webkit-text-stroke: 1.2px var(--white); letter-spacing: 1px; }
  .cta { position: absolute; left: 448px; top: 503px; width: 672px; text-align: right;
    font-family: "Audiowide", sans-serif; font-size: 17px; letter-spacing: 7px; color: var(--white); }
  .phone { position: absolute; left: 600px; top: 528px; width: 518px; text-align: right;
    font-weight: 700; font-style: italic; font-size: 46px; letter-spacing: 17px; color: #222; }
  .brand-name { position: absolute; left: 490px; top: 666px; font-weight: 700; font-size: 74px;
    line-height: 0.92; color: var(--ink); }
  .brand-mark { position: absolute; left: 858px; top: 676px; width: 176px; height: 176px;
    border-radius: 50%; background: var(--ink); }
  .site { position: absolute; left: 490px; top: 822px; font-weight: 500; font-size: 29px;
    line-height: 1.2; color: var(--green-bright); }
  .foot-bar { position: absolute; left: 0; top: 862px; width: 1200px; height: 38px; background: var(--green-dark); }
</style>
</head>
<body>
<main class="sign">
  <header class="sector-bar">
    <div class="sector">
      <svg viewBox="0 0 66 66"><circle cx="33" cy="33" r="30" fill="none" stroke="#fff" stroke-width="3.5"/><path d="M18 31 L33 19 L48 31 V46 H18 Z" fill="#fff"/><rect x="28" y="34" width="10" height="12" fill="#137a3b"/></svg>
      COMMERCIAL
    </div>
    <div class="sector">
      <svg viewBox="0 0 66 66"><circle cx="33" cy="33" r="30" fill="none" stroke="#fff" stroke-width="3.5"/><path d="M19 33 L33 20 L47 33 H43 V46 H23 V33 Z" fill="#fff"/><rect x="29" y="35" width="8" height="8" fill="#137a3b"/></svg>
      RESIDENTIAL
    </div>
    <div class="sector">
      <svg viewBox="0 0 66 66"><circle cx="33" cy="33" r="30" fill="none" stroke="#fff" stroke-width="3.5"/><path d="M17 46 V28 L27 34 V28 L37 34 V18 H42 V34 H49 V46 Z" fill="#fff"/></svg>
      INDUSTRIAL
    </div>
  </header>

  <div class="stripes"><span></span><span></span><span></span><span></span></div>

  <div class="mascot" role="img" aria-label="Green tornado mascot illustration"></div>

  <h2 class="col-head" style="left:390px">REMOVES:</h2>
  <h2 class="col-head" style="left:752px">SURFACES:</h2>

  <ul class="list" style="left:490px">
    <li><svg viewBox="0 0 36 30"><path d="M3 16 L13 26 L33 3" fill="none" stroke="#1a8a45" stroke-width="5"/></svg>PAINT</li>
    <li><svg viewBox="0 0 36 30"><path d="M3 16 L13 26 L33 3" fill="none" stroke="#1a8a45" stroke-width="5"/></svg>PRIMER</li>
    <li><svg viewBox="0 0 36 30"><path d="M3 16 L13 26 L33 3" fill="none" stroke="#1a8a45" stroke-width="5"/></svg>EPOXY</li>
    <li><svg viewBox="0 0 36 30"><path d="M3 16 L13 26 L33 3" fill="none" stroke="#1a8a45" stroke-width="5"/></svg>RUST</li>
    <li><svg viewBox="0 0 36 30"><path d="M3 16 L13 26 L33 3" fill="none" stroke="#1a8a45" stroke-width="5"/></svg>ALGAE</li>
    <li><svg viewBox="0 0 36 30"><path d="M3 16 L13 26 L33 3" fill="none" stroke="#1a8a45" stroke-width="5"/></svg>GREASE/GRIME</li>
    <li><svg viewBox="0 0 36 30"><path d="M3 16 L13 26 L33 3" fill="none" stroke="#1a8a45" stroke-width="5"/></svg>REMOVE GRAFFITI</li>
    <li><svg viewBox="0 0 36 30"><path d="M3 16 L13 26 L33 3" fill="none" stroke="#1a8a45" stroke-width="5"/></svg>AGEING FROM WOOD</li>
  </ul>

  <ul class="list" style="left:814px">
    <li><svg viewBox="0 0 36 30"><path d="M3 16 L13 26 L33 3" fill="none" stroke="#1a8a45" stroke-width="5"/></svg>HOME</li>
    <li><svg viewBox="0 0 36 30"><path d="M3 16 L13 26 L33 3" fill="none" stroke="#1a8a45" stroke-width="5"/></svg>AUTO</li>
    <li><svg viewBox="0 0 36 30"><path d="M3 16 L13 26 L33 3" fill="none" stroke="#1a8a45" stroke-width="5"/></svg>HEAVY EQUIPMENT</li>
    <li><svg viewBox="0 0 36 30"><path d="M3 16 L13 26 L33 3" fill="none" stroke="#1a8a45" stroke-width="5"/></svg>FARM EQUIPMENT</li>
    <li><svg viewBox="0 0 36 30"><path d="M3 16 L13 26 L33 3" fill="none" stroke="#1a8a45" stroke-width="5"/></svg>FIBERGLASS/BOAT</li>
    <li><svg viewBox="0 0 36 30"><path d="M3 16 L13 26 L33 3" fill="none" stroke="#1a8a45" stroke-width="5"/></svg>GARAGE FLOOR</li>
    <li><svg viewBox="0 0 36 30"><path d="M3 16 L13 26 L33 3" fill="none" stroke="#1a8a45" stroke-width="5"/></svg>STONE/BRICK/PATIOS</li>
    <li><svg viewBox="0 0 36 30"><path d="M3 16 L13 26 L33 3" fill="none" stroke="#1a8a45" stroke-width="5"/></svg>DECK/FENCE</li>
  </ul>

  <p class="more">...AND SO MUCH MORE!</p>
  <p class="cta">SCHEDULE A FREE ESTIMATE TODAY!</p>
  <p class="phone">555-204-3187</p>

  <p class="brand-name">HALDEN<br>STRIP CO.</p>
  <div class="brand-mark"></div>
  <p class="site">HTTPS://HALDENSTRIP.COM</p>

  <div class="foot-bar"></div>
</main>
</body>
</html>
```